Marigold Haven - Foundation PPT

Design a cohesive, emotionally resonant PowerPoint template that reflects the heart of Marigold Haven Pregnancy & Family Support. This template will be used across fundraising, partnership, and storytelling presentations, and must balance professionalism with warmth, compassion, and human connection.

Background
Marigold Haven Pregnancy & Family Support exists to support families navigating complicated pregnancies, prolonged hospital stays, and loss. The brand is rooted in empathy, quiet strength, and the concept of a “web” of care—an interconnected support system that surrounds families during difficult moments.

The template should feel deeply personal and mission-driven, not corporate.

Design Goals
Create a visually cohesive slide system that can be reused across multiple presentation types

Capture the emotional tone of the organization:
-Warm
-Gentle
-Hopeful
-Supportive
Ensure the design is clean, minimal, and easy to use for non-designers
Maintain a balance between storytelling and credibility

Key Design Requirements
-Brand Integration: Incorporate the Marigold Haven logo (provided)
Align with soft, neutral color palette (e.g., cream, sage, blush, light sky tones)
-Use elegant, readable typography

Slide Templates to Include
-Cover Slide (emotion-forward, minimal text)
-Mission / Story Slide
-Program Overview Slide
-Impact / Metrics Slide
-Partnership / Sponsor Slide
-“Web of Support” Concept Slide (visual representation of interconnected care)
-Call to Action Slide
-Optional: Quote/Testimonial Slide

Visual Style
-Soft, calming, and approachable aesthetic
-Use of whitespace to avoid clutter
-Light use of icons or illustrations (if applicable)
-Avoid overly corporate or overly busy design elements

Usability
-Fully editable in PowerPoint
-Clear text hierarchy and placeholders
-Easy for internal team to update content without design support
-Tone & Emotional Direction

This is not a clinical or corporate presentation—it should feel human, heartfelt, and intentional.

website: https://www.marigoldhavencare.org

```html
<!DOCTYPE html>
<html lang="en">
<head>
<meta charset="utf-8">
<title>Marigold Haven – Foundation Slide Template</title>
<link href="https://fonts.googleapis.com/css2?family=Inter:wght@300;400;500;600;700&display=swap" rel="stylesheet">
<style>
:root{
  --backdrop:#bd8a8c;
  --cream:#f3ece4;
  --card:#f4f0ea;
  --stone:#e9e5da;
  --white:#ffffff;
  --purple:#8e55a3;
  --purple-deep:#8f4ea5;
  --teal:#6a8e96;
  --ink:#2f2a2c;
  --mist:#e7f3f4;
  --blush:#c98a8e;
}
*{margin:0;padding:0;box-sizing:border-box}
html,body{width:1027px;height:1200px;overflow:hidden}
body{background:var(--backdrop);font-family:"Inter",sans-serif;color:var(--ink);position:relative}
.slide{position:absolute;width:438px;height:246px;overflow:hidden;background:var(--white)}
.abs{position:absolute}

/* brand */
.brand{position:absolute;display:flex;align-items:center;gap:4px;font-weight:600;color:var(--purple);white-space:nowrap}
.brand .dot{width:7px;height:7px;border-radius:50%;background:var(--purple)}
.slide-head .brand{left:14px;top:19px;font-size:11px}
.slide-head .rule{position:absolute;left:127px;top:9px;width:1px;height:32px;background:var(--purple);opacity:.6}
.slide-head .heading{position:absolute;left:140px;top:15px;font-size:14px;font-weight:600;color:var(--teal)}
.corner-deco{position:absolute;width:34px;height:34px;background:var(--teal);opacity:.12;border-radius:4px}

/* cover */
.cover{left:65px;top:74px;background:var(--cream)}
.cover .brand{left:20px;top:24px;font-size:16px}
.cover .brand .dot{width:9px;height:9px}
.cover-title{position:absolute;left:20px;top:80px;width:220px;font-size:20px;line-height:25px;font-weight:600;color:var(--purple)}
.cover-sub{position:absolute;left:21px;top:166px;width:210px;font-size:8.5px;line-height:13px;color:var(--ink)}
.cover-url{position:absolute;left:21px;top:207px;height:17px;padding:0 7px;background:var(--purple);color:var(--white);font-size:8px;line-height:17px}
.cover-web{left:284px;top:0;width:154px;height:237px;background:linear-gradient(135deg,rgba(106,142,150,.10),rgba(106,142,150,.28));border-bottom-left-radius:120px}

/* mission */
.mission{left:523px;top:73px}
.mission-copy{position:absolute;left:20px;top:66px;width:171px;text-align:right;font-size:6.6px;line-height:11px}
.mission-copy p+p{margin-top:11px}
.mission-bar{left:213px;top:65px;width:5px;height:131px;background:var(--purple)}
.mission-photo{left:215px;top:0;width:223px;height:246px;background:radial-gradient(circle at 30% 15%,#c9a2c4 0,#6d5b9c 30%,#243a8a 55%,#10131f 85%)}
.heart{position:absolute;width:9px;height:8px}

/* program */
.program{left:65px;top:340px}
.prog-card{position:absolute;top:58px;width:98px;height:174px;background:var(--card);padding:12px 10px 0 12px;display:flex;flex-direction:column}
.prog-card svg{width:24px;height:22px;flex:none}
.prog-card h3{margin-top:18px;font-size:8.4px;line-height:10px;font-weight:600;color:var(--purple)}
.prog-card p{margin-top:6px;font-size:5.3px;line-height:7.7px}

/* impact */
.impact{left:523px;top:342px;background:var(--stone)}
.grid-h{left:14px;top:139px;width:399px;height:1px;background:var(--purple);opacity:.5}
.grid-v{left:216px;top:61px;width:1px;height:159px;background:var(--purple);opacity:.5}
.stat-num{position:absolute;font-size:17px;font-weight:600;color:var(--purple)}
.stat-rule{position:absolute;width:1px;height:44px;background:var(--purple);opacity:.6}
.stat-text{position:absolute;width:115px}
.stat-text h3{font-size:9px;line-height:10.5px;font-weight:600;color:var(--purple)}
.stat-text p{margin-top:4px;font-size:6.8px;line-height:10px}

/* partnership */
.partner{left:65px;top:609px}
.partner-photo{left:15px;top:57px;width:194px;height:170px;border-radius:4px;background:linear-gradient(135deg,#c9c6bf 0,#8c8882 45%,#3d3a3c 100%)}
.partner-copy{position:absolute;left:226px;top:56px;width:182px;font-size:6.5px;line-height:11px}
.partner-copy p+p{margin-top:11px}
.partner-box{position:absolute;left:226px;top:131px;width:148px;height:97px;background:var(--mist);border-radius:6px;padding:9px 8px 9px 13px}
.partner-box h3{font-size:6.8px;font-weight:600;color:var(--teal);margin-bottom:6px}
.partner-box li{list-style:none;display:flex;align-items:center;gap:6px;font-size:6.3px;height:15px;white-space:nowrap}
.partner-box li svg{width:8px;height:8px;flex:none}

/* web of support */
.web{left:522px;top:607px}
.web .brand{left:14px;top:23px;font-size:11px}
.web-title{position:absolute;left:16px;top:69px;font-size:14px;font-weight:600;color:var(--teal)}
.web-copy{position:absolute;left:16px;top:95px;width:160px;font-size:5.9px;line-height:9.6px;text-align:justify}
.web-art{left:270px;top:58px;width:140px;height:158px;background:radial-gradient(circle at 20% 85%,rgba(106,142,150,.30),rgba(106,142,150,.08) 75%);border-radius:6px}
.web-label{position:absolute;font-size:6.8px;line-height:8.5px;color:var(--teal);text-align:center;transform:translateX(-50%)}

/* testimonial */
.testimonial{left:67px;top:880px;background:var(--cream)}
.quote-panel{position:absolute;left:19px;top:60px;width:400px;height:175px;background:var(--white);box-shadow:0 0 4px rgba(0,0,0,.06)}
.quote-card{position:absolute;top:71px;width:185px;height:155px;border:1px solid #ece8e2;background:var(--white);padding:22px 10px 0 27px;display:flex;flex-direction:column}
.quote-card .mark{position:absolute;left:9px;top:4px;font-size:16px;font-weight:700;color:var(--purple)}
.quote-card p{font-size:5.3px;line-height:8.6px}
.quote-card .name{margin-top:6px;font-size:5.8px;font-weight:600;color:var(--purple)}
.butterfly-spot{left:388px;top:22px;width:34px;height:36px;border-radius:50%;background:linear-gradient(135deg,#a77cb6,var(--blush));opacity:.85}

/* thank you */
.thanks{left:526px;top:880px;background:var(--purple-deep)}
.thanks .brand{left:50%;top:52px;transform:translateX(-50%);color:var(--white);font-size:22px;font-weight:500;gap:7px}
.thanks .brand .dot{background:var(--white);width:11px;height:11px}
.thanks-rule{left:133px;width:155px;height:1px;background:var(--white);opacity:.8}
.thanks-text{position:absolute;left:0;top:144px;width:100%;text-align:center;font-size:29px;font-weight:300;color:var(--white)}
</style>
</head>
<body>

<!-- Cover -->
<section class="slide cover">
  <div class="brand"><span class="dot"></span>Marigold Haven</div>
  <h1 class="cover-title">Marigold Haven Pregnancy &amp; Family Support</h1>
  <p class="cover-sub">Supporting Families Through Complex Pregnancies, Hospital Journeys, and Loss</p>
  <div class="cover-url">www.marigoldhavencare.org</div>
  <div class="abs cover-web" role="img" aria-label="Large sage web illustration"></div>
</section>

<!-- Mission -->
<section class="slide mission">
  <div class="slide-head">
    <div class="brand"><span class="dot"></span>Marigold Haven</div>
    <div class="rule"></div>
    <h2 class="heading">Mission</h2>
  </div>
  <div class="mission-copy">
    <p>Every pregnancy journey is different.<br>Some families face unexpected complications,<br>extended hospital stays, and heartbreaking loss.</p>
    <p>Marigold Haven Pregnancy &amp; Family Support was<br>created to ensure that no family walks these difficult<br>paths alone.</p>
    <p>Through compassion, connection, and practical<br>support, we surround families with a web of<br>care—helping them navigate some of the most<br>vulnerable moments of their lives.</p>
  </div>
  <div class="abs mission-bar"></div>
  <svg class="heart" style="left:177px;top:224px" viewBox="0 0 10 9"><path d="M5 9 0.8 4.6A2.4 2.4 0 0 1 5 1.6a2.4 2.4 0 0 1 4.2 3Z" fill="var(--blush)"/></svg>
  <div class="corner-deco" style="left:0;top:212px"></div>
  <div class="abs mission-photo" role="img" aria-label="Photo of white butterflies resting on blue blossoms"></div>
</section>

<!-- Program Overview -->
<section class="slide program">
  <div class="slide-head">
    <div class="brand"><span class="dot"></span>Marigold Haven</div>
    <div class="rule"></div>
    <h2 class="heading">Program Overview</h2>
  </div>
  <div class="corner-deco" style="left:404px;top:0"></div>
  <article class="prog-card" style="left:12px">
    <svg viewBox="0 0 24 22"><path d="M12 21 2.5 11.5A5.5 5.5 0 0 1 12 4a5.5 5.5 0 0 1 9.5 7.5Z" fill="var(--teal)"/></svg>
    <h3>Family Support</h3>
    <p>Personal guidance and emotional support for families experiencing complex pregnancies or neonatal hospital stays. Lorem ipsum dolor sit amet, consectetur adipiscing elit, sed do eiusmod tempor incididunt ut labore et dolore magna aliqua. Ut enim ad minim veniam, quis nostrud exercitation ullamco laboris nisi</p>
  </article>
  <article class="prog-card" style="left:119px">
    <svg viewBox="0 0 24 22" fill="none" stroke="var(--teal)" stroke-width="1.6"><circle cx="12" cy="4" r="3"/><circle cx="4" cy="11" r="3"/><circle cx="20" cy="11" r="3"/><circle cx="12" cy="18" r="3"/></svg>
    <h3>Community Connection</h3>
    <p>Personal guidance and emotional support for families experiencing complex pregnancies or neonatal hospital stays. Lorem ipsum dolor sit amet, consectetur adipiscing elit, sed do eiusmod tempor incididunt ut labore et dolore magna aliqua. Ut enim ad minim veniam, quis</p>
  </article>
  <article class="prog-card" style="left:225px">
    <svg viewBox="0 0 24 22"><path d="M2 6 8 3l4 3 4-3 6 3v6l-10 8L2 12Z" fill="var(--teal)"/></svg>
    <h3>Loss Support</h3>
    <p>Personal guidance and emotional support for families experiencing complex pregnancies or neonatal hospital stays. Lorem ipsum dolor sit amet, consectetur adipiscing elit, sed do eiusmod tempor incididunt ut labore et dolore magna aliqua. Ut enim ad minim veniam, quis nostrud exercitation ullamco laboris nisi</p>
  </article>
  <article class="prog-card" style="left:330px">
    <svg viewBox="0 0 24 22"><path d="M2 9h4l10-6v16L6 13H2Z" fill="var(--teal)"/><path d="M18 6l4-3M19 11h4M18 16l4 3" stroke="var(--teal)" stroke-width="1.4"/></svg>
    <h3>Advocacy &amp; Awareness</h3>
    <p>Personal guidance and emotional support for families experiencing complex pregnancies or neonatal hospital stays. Lorem ipsum dolor sit amet, consectetur adipiscing elit, sed do eiusmod tempor incididunt ut labore et dolore magna aliqua. Ut enim ad minim veniam, quis</p>
  </article>
</section>

<!-- Impact -->
<section class="slide impact">
  <div class="slide-head">
    <div class="brand"><span class="dot"></span>Marigold Haven</div>
    <div class="rule"></div>
    <h2 class="heading">Impact</h2>
  </div>
  <div class="corner-deco" style="left:404px;top:0"></div>
  <div class="corner-deco" style="left:0;top:212px"></div>
  <div class="abs grid-h"></div>
  <div class="abs grid-v"></div>

  <div class="stat-num" style="left:21px;top:83px">1258</div>
  <div class="stat-rule" style="left:74px;top:71px"></div>
  <div class="stat-text" style="left:89px;top:72px"><h3>Families Supported</h3><p>Providing emotional and practical support during complex pregnancy journeys.</p></div>

  <div class="stat-num" style="left:236px;top:83px">2400</div>
  <div class="stat-rule" style="left:290px;top:71px"></div>
  <div class="stat-text" style="left:305px;top:72px"><h3>Hospital Partnerships</h3><p>Working alongside medical teams to support families through long NICU stays.</p></div>

  <div class="stat-num" style="left:21px;top:176px">3210</div>
  <div class="stat-rule" style="left:74px;top:163px"></div>
  <div class="stat-text" style="left:89px;top:164px"><h3>Community Connections Made</h3><p>Helping families find comfort in shared experiences.</p></div>

  <div class="stat-num" style="left:230px;top:176px">10241</div>
  <div class="stat-rule" style="left:290px;top:163px"></div>
  <div class="stat-text" style="left:305px;top:164px"><h3>Support Resources Provided</h3><p>Guides, connections, and ongoing support.</p></div>
</section>

<!-- Partnership -->
<section class="slide partner">
  <div class="slide-head">
    <div class="brand"><span class="dot"></span>Marigold Haven</div>
    <div class="rule"></div>
    <h2 class="heading">Partnership</h2>
  </div>
  <div class="corner-deco" style="left:404px;top:0"></div>
  <div class="abs partner-photo" role="img" aria-label="Photo of hands joining puzzle pieces together"></div>
  <div class="partner-copy">
    <p>Supporting families during difficult pregnancies requires a strong network of compassionate partners.</p>
    <p>Marigold Haven collaborates with healthcare providers, community organizations, and supporters who believe every family deserves care, dignity, and connection.</p>
  </div>
  <div class="partner-box">
    <h3>Partnership Opportunities</h3>
    <ul>
      <li><svg viewBox="0 0 8 8"><path d="M4 0v8M0.6 2l6.8 4M0.6 6l6.8-4" stroke="var(--purple)" stroke-width="1.6"/></svg>Hospital &amp; healthcare partnerships</li>
      <li><svg viewBox="0 0 8 8"><path d="M4 0v8M0.6 2l6.8 4M0.6 6l6.8-4" stroke="var(--purple)" stroke-width="1.6"/></svg>Community collaboration</li>
      <li><svg viewBox="0 0 8 8"><path d="M4 0v8M0.6 2l6.8 4M0.6 6l6.8-4" stroke="var(--purple)" stroke-width="1.6"/></svg>Corporate sponsorship</li>
      <li><svg viewBox="0 0 8 8"><path d="M4 0v8M0.6 2l6.8 4M0.6 6l6.8-4" stroke="var(--purple)" stroke-width="1.6"/></svg>Event and fundraising partnerships</li>
    </ul>
  </div>
</section>

<!-- Web of Support -->
<section class="slide web">
  <div class="brand"><span class="dot"></span>Marigold Haven</div>
  <h2 class="web-title">Web of Support</h2>
  <p class="web-copy">Sed ut perspiciatis unde omnis iste natus error sit voluptatem accusantium doloremque laudantium, totam rem aperiam, eaque ipsa quae ab illo inventore veritatis et quasi architecto beatae vitae dicta sunt explicabo. Nemo enim ipsam voluptatem quia voluptas sit aspernatur aut odit aut fugit, sed quia consequuntur magni dolores eos qui ratione voluptatem sequi nesciunt. Neque porro quisquam est, qui dolorem ipsum quia dolor sit amet, consectetur, adipisci velit, sed quia non numquam eius modi tempora incidunt ut labore et dolore magnam aliquam quaerat voluptatem. Ut enim ad minima veniam, quis nostrum exercitationem ullam corporis.</p>
  <div class="abs web-art" role="img" aria-label="Web illustration linking the circles of care"></div>
  <span class="web-label" style="left:301px;top:33px">Emotional<br>Care</span>
  <span class="web-label" style="left:379px;top:30px">Resources &amp;<br>Guidance</span>
  <span class="web-label" style="left:246px;top:79px">Peer<br>Families</span>
  <span class="web-label" style="left:225px;top:142px">Community<br>Support</span>
  <span class="web-label" style="left:262px;top:189px">Medical<br>Teams</span>
  <span class="web-label" style="left:322px;top:214px">Advocacy</span>
</section>

<!-- Testimonial -->
<section class="slide testimonial">
  <div class="slide-head">
    <div class="brand"><span class="dot"></span>Marigold Haven</div>
    <div class="rule"></div>
    <h2 class="heading">Testimonial</h2>
  </div>
  <div class="abs butterfly-spot" role="img" aria-label="Butterfly illustration"></div>
  <div class="quote-panel"></div>
  <div class="corner-deco" style="left:0;top:212px"></div>
  <div class="corner-deco" style="left:404px;top:212px"></div>
  <blockquote class="quote-card" style="left:29px">
    <span class="mark">“</span>
    <p>At vero eos et accusamus et iusto odio dignissimos ducimus qui blanditiis praesentium voluptatum deleniti atque corrupti quos dolores et quas molestias excepturi sint occaecati cupiditate non provident, similique sunt in culpa qui officia deserunt mollitia animi, id est laborum et dolorum fuga. Et harum quidem rerum facilis est et expedita distinctio. Nam libero tempore, cum soluta nobis est eligendi optio cumque nihil impeditquo minus id quod maxime placeat facere possimus, omnis voluptas assumenda est, omnis dolor repellendus. Temporibus autem quibusdam</p>
    <span class="name">ELENA</span>
  </blockquote>
  <blockquote class="quote-card" style="left:222px">
    <span class="mark">“</span>
    <p>At vero eos et accusamus et iusto odio dignissimos ducimus qui blanditiis praesentium voluptatum deleniti atque corrupti quos dolores et quas molestias excepturi sint occaecati cupiditate non provident, similique sunt in culpa qui officia deserunt mollitia animi, id est laborum et dolorum fuga. Et harum quidem rerum facilis est et expedita distinctio. Nam libero tempore, cum soluta nobis est eligendi optio cumque nihil impeditquo minus id quod maxime placeat facere possimus, omnis voluptas assumenda est, omnis dolor repellendus. Temporibus autem quibusdam</p>
    <span class="name">ELENA</span>
  </blockquote>
</section>

<!-- Thank You -->
<section class="slide thanks">
  <svg class="heart" style="left:12px;top:16px;width:30px;height:27px" viewBox="0 0 10 9"><path d="M5 9 0.8 4.6A2.4 2.4 0 0 1 5 1.6a2.4 2.4 0 0 1 4.2 3Z" fill="var(--white)"/></svg>
  <div class="brand"><span class="dot"></span>Marigold Haven</div>
  <div class="abs thanks-rule" style="top:136px"></div>
  <div class="thanks-text">Thank You</div>
  <div class="abs thanks-rule" style="top:194px"></div>
</section>

</body>
</html>
```